Plinthmoor Assessments Landing Page

We need a landing page re-designed for a new website www.plinthmoorassessments.example and the website is live if you search the address provided.
We need the industry standard files for embedding this into the landing page of our website. The company is a real estate advisory firm, we provide professional property services and are focused on business rates (commercial property taxation in the UK).
We have uploaded a file which is meant to provide a visual guide as to how we envisage the landing page looking. You are free to come up with an entirely different creative design. The image at the top with the search button is taken from another website so the design will need to be distinctly different but may follow the same theme. Furthermore, the colour palette does not need to be followed slavishly and can be modified changed and improved upon. It might be that you want to incorporate other visual cues such as a desktop PC, laptop and iPad as these are devices the website will be accessed from; however, this is not essential and only a guide.
**To clarify, please note, the target industry is commercial properties and not residential or domestic property, so please when incorporating designs of buildings its important to focus on commercial property such as shops, offices, industrial buildings etc.**
Target Market(s)
Occupiers of commercial real estate in the UK who pay property tax to occupy the property.
Look and feel
Each slider illustrates characteristics of the customer's brand and the style your logo design should communicate.

```html
<!DOCTYPE html>
<html lang="en">
<head>
<meta charset="utf-8">
<title>Plinthmoor Assessments</title>
<link rel="stylesheet" href="https://fonts.googleapis.com/css2?family=Montserrat:wght@500;600;700&family=Roboto:wght@300;400;500;700&display=swap">
<style>
:root{
  --orange:#f26b1d;
  --orange-soft:#fde7d8;
  --navy:#121a5c;
  --navy-deep:#0a0f3d;
  --page:#f3f6fb;
  --ink:#1e2233;
  --muted:#c9cde6;
  --white:#ffffff;
}
*{margin:0;padding:0;box-sizing:border-box}
html,body{width:1200px;height:3193px;overflow:hidden}
body{position:relative;background:var(--page);font-family:'Roboto',sans-serif;color:var(--ink)}
.abs{position:absolute}

/* utility bar */
.utility{left:0;top:0;width:1200px;height:46px;background:var(--navy-deep)}
.utility-contact{left:45px;top:15px;color:var(--white);font-family:'Montserrat',sans-serif;font-weight:600;font-size:13px;letter-spacing:1px}
.utility-social{top:14px;width:18px;height:18px;border:2px solid var(--orange)}
.utility-account{left:760px;top:15px;display:flex;gap:24px;color:var(--muted);font-size:13px;letter-spacing:.5px}
.utility-cta{left:1005px;top:0;width:150px;height:46px;background:var(--orange);color:var(--white);font-family:'Montserrat',sans-serif;font-weight:700;font-size:13px;letter-spacing:.5px;display:flex;align-items:center;justify-content:center}

/* header */
.header{left:0;top:46px;width:1200px;height:80px;background:var(--white)}
.brand{left:45px;top:71px;display:flex;align-items:center;gap:12px;color:var(--navy);font-family:'Montserrat',sans-serif;font-weight:600;font-size:20px;line-height:30px}
.brand-mark{width:30px;height:30px;background:var(--orange);display:block}
.nav{left:700px;top:76px;display:flex;gap:34px;color:var(--navy);font-family:'Montserrat',sans-serif;font-weight:600;font-size:14px;line-height:20px}
.accreditation{left:1115px;top:70px;width:40px;height:32px;border-radius:50%;background:#d9dcea}

/* hero */
.hero{left:0;top:126px;width:1200px;height:560px;background:var(--navy)}
.hero-photo{left:640px;top:126px;width:560px;height:560px;background:linear-gradient(160deg,#9b2f45 0%,#6b6fa8 45%,#b7bdd6 100%);clip-path:polygon(90px 0,100% 0,100% 100%,0 100%)}
.hero-stripe{left:622px;top:126px;width:14px;height:560px;background:var(--orange);clip-path:polygon(90px 0,100% 0,0 100%,0 100%);transform:skewX(-9deg);transform-origin:bottom left}
.hero-title{left:60px;top:200px;width:560px;color:var(--white);font-family:'Montserrat',sans-serif;font-weight:700;font-size:48px;line-height:58px}
.hero-title em{font-style:normal;color:var(--orange)}
.hero-sub{left:62px;top:398px;width:470px;color:var(--muted);font-size:16px;line-height:26px;font-weight:300}
.search{left:60px;top:508px;width:400px;height:54px;background:var(--white);display:flex;align-items:center;padding-left:16px;gap:12px;color:#9a9db0;font-size:14px}
.search svg{flex:none}
.search-btn{left:460px;top:508px;width:150px;height:54px;background:var(--orange);color:var(--white);font-family:'Montserrat',sans-serif;font-weight:700;font-size:14px;display:flex;align-items:center;justify-content:center}

/* service cards */
.card{top:730px;width:350px;height:300px;background:var(--white);border-top:4px solid var(--orange)}
.card-icon{position:absolute;left:30px;top:30px;width:64px;height:64px;background:var(--orange-soft);display:flex;align-items:center;justify-content:center}
.card p{position:absolute;left:30px;top:114px;width:290px;font-size:17px;line-height:27px;color:var(--ink)}
.card .more{position:absolute;left:30px;top:246px;color:var(--orange);font-family:'Montserrat',sans-serif;font-weight:700;font-size:14px;letter-spacing:1px;display:flex;align-items:center;gap:8px;line-height:20px}

/* benefits */
.section-title{left:60px;top:1092px;font-family:'Montserrat',sans-serif;font-weight:700;font-size:34px;line-height:42px;color:var(--navy)}
.section-rule{left:60px;top:1142px;width:60px;height:5px;background:var(--orange)}
.benefit-photo{width:540px;height:330px}
.benefit{width:570px;height:330px;background:var(--white);padding:48px 44px}
.benefit h3{font-family:'Montserrat',sans-serif;font-size:18px;line-height:24px;font-weight:700;color:var(--navy);margin-bottom:18px}
.benefit p{font-size:17px;line-height:28px;color:var(--ink)}

.tagline{left:60px;top:2300px;width:1000px;padding-left:26px;border-left:6px solid var(--orange);color:var(--navy);font-family:'Montserrat',sans-serif;font-weight:700;font-size:24px;line-height:34px}

/* call to action */
.cta{left:45px;top:2440px;width:1110px;height:160px;background:var(--orange)}
.cta h2{position:absolute;left:50px;top:40px;color:var(--white);font-family:'Montserrat',sans-serif;font-weight:700;font-size:34px;line-height:42px}
.cta p{position:absolute;left:50px;top:90px;color:var(--white);font-size:18px;line-height:26px;font-weight:300}
.cta .book{position:absolute;left:800px;top:48px;width:260px;height:64px;background:var(--navy-deep);color:var(--white);font-family:'Montserrat',sans-serif;font-weight:700;font-size:22px;letter-spacing:1px;display:flex;align-items:center;justify-content:center}

.skyline{left:45px;top:2690px;width:1110px;height:260px;background:linear-gradient(180deg,#f3f6fb 0%,#cfe0f6 55%,#7fa9e3 100%)}

/* footer */
.footer-top{left:0;top:2997px;width:1200px;height:99px;background:var(--navy)}
.footer-info{left:45px;top:3026px;color:var(--white);font-family:'Montserrat',sans-serif;font-weight:500;font-size:15px;line-height:22px}
.follow{left:870px;top:3036px;color:var(--white);font-family:'Montserrat',sans-serif;font-weight:700;font-size:18px;line-height:24px}
.footer-social{top:3033px;width:30px;height:30px;border:2px solid var(--orange)}
.footer-bottom{left:0;top:3096px;width:1200px;height:97px;background:var(--navy-deep)}
.copyright{left:45px;top:3136px;color:var(--muted);font-size:14px;line-height:18px}
.footer-links{left:678px;top:3135px;display:flex;gap:31px;color:var(--white);font-weight:700;font-size:15px;line-height:20px}
</style>
</head>
<body>

<header>
  <div class="abs utility"></div>
  <div class="abs utility-contact">CONTACT US</div>
  <div class="abs utility-social" style="left:170px" aria-label="Social profile"></div>
  <div class="abs utility-social" style="left:198px" aria-label="Social profile"></div>
  <div class="abs utility-social" style="left:226px" aria-label="Social profile"></div>
  <div class="abs utility-account"><span>MY ACCOUNT</span><span>LOGOUT</span></div>
  <div class="abs utility-cta">BOOK VALUATION</div>

  <div class="abs header"></div>
  <div class="abs brand"><i class="brand-mark"></i>Plinthmoor Assessments</div>
  <nav class="abs nav"><span>PROPERTY SEARCH</span><span>DISCOVER</span><span>ABOUT</span></nav>
  <div class="abs accreditation" aria-label="Accreditation badge"></div>
</header>

<section>
  <div class="abs hero"></div>
  <div class="abs hero-photo" role="img" aria-label="Modern commercial office building with red cladding"></div>
  <h1 class="abs hero-title">Do You Think Your<br>Business Rates Are<br><em>Too High?</em></h1>
  <p class="abs hero-sub">Use our free valuation tool below or book a valuation with one of our qualified surveyors. No shock commissions and fair fixed fees from $295!</p>
  <div class="abs search">
    <svg width="18" height="18" viewBox="0 0 18 18"><circle cx="7.5" cy="7.5" r="5.5" fill="none" stroke="#9a9db0" stroke-width="1.6"/><line x1="11.5" y1="11.5" x2="16" y2="16" stroke="#9a9db0" stroke-width="1.6"/></svg>
    Enter your commercial property postcode to begin
  </div>
  <div class="abs search-btn">GET STARTED</div>
</section>

<section>
  <div class="abs card" style="left:45px">
    <div class="card-icon"><svg width="40" height="34" viewBox="0 0 90 76" fill="none" stroke="#121a5c" stroke-width="5"><rect x="4" y="4" width="82" height="54" rx="3"/><line x1="45" y1="58" x2="45" y2="70"/><line x1="26" y1="72" x2="64" y2="72"/></svg></div>
    <p>We offer a free online valuation tool which will help you better understand your rateable valuation and rates payable.</p>
    <div class="more">READ MORE <svg width="16" height="10" viewBox="0 0 16 10"><path d="M0 5h14M10 1l4 4-4 4" fill="none" stroke="#f26b1d" stroke-width="2"/></svg></div>
  </div>
  <div class="abs card" style="left:425px">
    <div class="card-icon"><svg width="36" height="36" viewBox="0 0 90 86" fill="none" stroke="#121a5c" stroke-width="6"><rect x="22" y="4" width="46" height="78"/><line x1="4" y1="82" x2="86" y2="82"/><g fill="#121a5c" stroke="none"><rect x="32" y="16" width="8" height="9"/><rect x="50" y="16" width="8" height="9"/><rect x="32" y="34" width="8" height="9"/><rect x="50" y="34" width="8" height="9"/></g><rect x="38" y="60" width="14" height="22"/></svg></div>
    <p>Use our free valuation tool to estimate the rateable value of your commercial property in England and Wales.</p>
    <div class="more">READ MORE <svg width="16" height="10" viewBox="0 0 16 10"><path d="M0 5h14M10 1l4 4-4 4" fill="none" stroke="#f26b1d" stroke-width="2"/></svg></div>
  </div>
  <div class="abs card" style="left:805px">
    <div class="card-icon"><svg width="32" height="36" viewBox="0 0 90 86" fill="none" stroke="#121a5c" stroke-width="6"><rect x="14" y="8" width="62" height="76" rx="4"/><rect x="32" y="2" width="26" height="12" rx="2"/><line x1="28" y1="34" x2="62" y2="34"/><line x1="28" y1="56" x2="62" y2="56"/></svg></div>
    <p>Need help? Book a qualified surveyor to advise you on the rateable value of your commercial property.</p>
    <div class="more">READ MORE <svg width="16" height="10" viewBox="0 0 16 10"><path d="M0 5h14M10 1l4 4-4 4" fill="none" stroke="#f26b1d" stroke-width="2"/></svg></div>
  </div>
</section>

<section>
  <h2 class="abs section-title">BENEFITS</h2>
  <div class="abs section-rule"></div>

  <div class="abs benefit-photo" style="left:45px;top:1190px;background:linear-gradient(135deg,#9fd6d4,#e3bd86 55%,#9fd6d4)" role="img" aria-label="Wooden figures grouped in a circle"></div>
  <div class="abs benefit" style="left:585px;top:1190px">
    <h3>WE’VE GOT YOU COVERED</h3>
    <p>Our rating list contains the most up-to-date information of around 2 million commercial properties in England and Wales. Our qualified rating surveyors provide nationwide coverage and we employ some of the highest qualified surveyors with some holding the Institute of Rating Diploma.</p>
  </div>

  <div class="abs benefit" style="left:45px;top:1550px">
    <h3>FAIR FIXED FEES &amp; NO SHOCK COMMISSIONS</h3>
    <p>Our fees are fixed up front, ensuring there are no surprises and we promise to never change any stock commissions. Not only does this provide you with certainty of cost, it also provides you with confidence that our surveyors are not lead by the prospect of large commission payments.</p>
  </div>
  <div class="abs benefit-photo" style="left:615px;top:1550px;background:linear-gradient(135deg,#c9cbc4,#d9a467 50%,#9ea89a)" role="img" aria-label="Letter tiles spelling save resting on banknotes"></div>

  <div class="abs benefit-photo" style="left:45px;top:1910px;background:linear-gradient(180deg,#1d4f9c,#4a86cf 60%,#dbe8f5)" role="img" aria-label="Signpost pointing to help, support, advice and guidance"></div>
  <div class="abs benefit" style="left:585px;top:1910px">
    <h3>STEP BY STEP GUIDANCE</h3>
    <p>We are here from initial point of contact right through to the end, be that to provide essential desktop valuation, on-site valuation or helping you through the Check, Challenge and Appeal proces. We’re here to support and guide you every step of the way.</p>
  </div>

  <p class="abs tagline">Our surveyors don’t do speculative appeals, we provide honest and<br>professional advice at a fair fixed fee</p>
</section>

<section class="abs cta">
  <h2>Book A Rateable Valuation</h2>
  <p>One of our qualified surveyors are eag to hear from you</p>
  <div class="book">BOOK NOW</div>
</section>

<div class="abs skyline" role="img" aria-label="Line illustration of a city skyline with office towers"></div>

<footer>
  <div class="abs footer-top"></div>
  <div class="abs footer-info">Company Registration Number: 10457316<br>Company Registered Address: Harbour Court, Quayside Park, Leeds LS9 4QT</div>
  <div class="abs follow">FOLLOW US</div>
  <div class="abs footer-social" style="left:1025px" aria-label="Social profile"></div>
  <div class="abs footer-social" style="left:1070px" aria-label="Social profile"></div>
  <div class="abs footer-social" style="left:1115px" aria-label="Social profile"></div>
  <div class="abs footer-bottom"></div>
  <div class="abs copyright">@ 2019 PLINTHMOOR ASSESSMENTS. ALL RIGHTS RESERVED</div>
  <nav class="abs footer-links"><span>PRICING PLANS</span><span>FAQ</span><span>CONTACT</span><span>LEGAL &amp; TERMS</span></nav>
</footer>

</body>
</html>
```